Esthetically Pleasing Core Values and Brand Promise for Accounting Firm

I would like a cohesive design that ties together my core values and brand promise. My firm, Maple Finch Advisory, provides accounting work to small businesses. I prefer modern and clean designs. I want my Core Values and Brand Promise to represent me - sole entrepreneur, married, mother of two kids, modern esthetics, clean lines, organized, colorful (teals, greys, white, yellows)

Industry/Entity Type

Public Accounting

Colors
33b8a4

```html
<!DOCTYPE html>
<html lang="en">
<head>
<meta charset="utf-8">
<title>Maple Finch Advisory — Core Values</title>
<link href="https://fonts.googleapis.com/css2?family=Oswald:wght@600;700&family=Lato:wght@400;700&family=Archivo+Black&display=swap" rel="stylesheet">
<style>
:root{
  --teal:#33b8a4;
  --teal-top:#21a992;
  --teal-deep:#126a5a;
  --green-ink:#17604f;
  --ink:#1f2a30;
  --white:#ffffff;
  --page:#eeeeec;
  --orange-a:#f6b51c;--orange-b:#f08a2a;
  --purple-a:#9a62b8;--purple-b:#6b3c8f;
  --green-a:#86c443;--green-b:#3f9a3a;
  --blue-a:#4a95db;--blue-b:#2363b3;
}
*{box-sizing:border-box;margin:0;padding:0}
html,body{width:1200px;height:1200px;overflow:hidden;background:var(--page)}
.poster{position:absolute;left:170px;top:15px;width:860px;height:1170px;background:var(--white);overflow:hidden}
.values-panel{position:absolute;left:23px;top:39px;width:811px;height:704px;
  background:linear-gradient(180deg,var(--teal-top),var(--teal-deep));overflow:hidden}
.values-strip{position:absolute;left:0;top:0;width:147px;height:100%;background:var(--teal)}
.values-title{position:absolute;left:73px;top:351px;transform:translate(-50%,-50%) rotate(-90deg);
  white-space:nowrap;font-family:"Archivo Black",sans-serif;font-weight:400;font-size:60px;line-height:1;letter-spacing:8px;color:var(--white)}
.brand-name{position:absolute;left:693px;top:23px;width:107px;height:83px;background:var(--white);
  display:flex;align-items:center;justify-content:center;text-align:center;
  font-family:"Lato",sans-serif;font-weight:700;font-size:15px;line-height:1.2;color:var(--teal)}
.connector{position:absolute;left:230px;top:165px;height:430px;border-left:3px dotted #e6f2ef}
.value{position:absolute;left:176px;width:600px;height:110px}
.value-badge{position:absolute;left:0;top:0;width:110px;height:110px;border-radius:50%;
  box-shadow:0 4px 10px rgba(0,0,0,.25)}
.badge-empower{background:radial-gradient(circle at 35% 30%,var(--orange-a),var(--orange-b))}
.badge-client{background:radial-gradient(circle at 35% 30%,var(--purple-a),var(--purple-b))}
.badge-rectitude{background:radial-gradient(circle at 35% 30%,var(--green-a),var(--green-b))}
.badge-relentless{background:radial-gradient(circle at 35% 30%,var(--blue-a),var(--blue-b))}
.value-text{position:absolute;left:125px;top:8px;width:440px;color:var(--white)}
.value-name{font-family:"Oswald",sans-serif;font-weight:700;font-size:32px;line-height:1.1;margin-bottom:6px}
.value-desc{font-family:"Lato",sans-serif;font-size:16px;line-height:1.25}
.value-desc b{font-size:21px;font-weight:400}
.promise{position:absolute;left:0;top:764px;width:860px;line-height:40px;text-align:center;
  font-family:"Oswald",sans-serif;font-weight:700;font-size:30px;color:var(--green-ink)}
.service{position:absolute;top:840px;width:320px;text-align:center}
.service-tax{left:33px}
.service-accounting{left:476px}
.service-art{width:172px;height:184px;margin:0 auto}
.art-tax{background:linear-gradient(180deg,#2c6db8 0 30%,#f4f6f8 30% 38%,#2b3a4a 38%)}
.art-accounting{background:linear-gradient(160deg,#f5b93a,#7aa5d8 45%,#4a5779)}
.service-desc{margin-top:30px;font-family:"Lato",sans-serif;font-size:15px;line-height:1.38;color:var(--ink)}
.divider{position:absolute;left:417px;top:856px;width:2px;height:281px;background:#3a3a3a}
.footer-band{position:absolute;left:0;bottom:0;width:860px;height:26px;background:var(--teal)}
</style>
</head>
<body>
<main class="poster">
  <section class="values-panel">
    <div class="values-strip"><h1 class="values-title">CORE VALUES</h1></div>
    <div class="brand-name">Maple Finch Advisory</div>
    <div class="connector"></div>

    <article class="value" style="top:110px">
      <div class="value-badge badge-empower" role="img" aria-label="Icon of an empowered person flexing"></div>
      <div class="value-text">
        <h2 class="value-name">Empower</h2>
        <p class="value-desc"><b>W</b>e are dedicated, appreciative and respectful of people’s time and purpose.</p>
      </div>
    </article>

    <article class="value" style="top:249px">
      <div class="value-badge badge-client" role="img" aria-label="Icon of a client in a target"></div>
      <div class="value-text">
        <h2 class="value-name">Client Focused</h2>
        <p class="value-desc"><b>W</b>e provide a personal service that goes above the standards of professional care.</p>
      </div>
    </article>

    <article class="value" style="top:393px">
      <div class="value-badge badge-rectitude" role="img" aria-label="Icon of scales of justice"></div>
      <div class="value-text">
        <h2 class="value-name">Rectitude</h2>
        <p class="value-desc"><b>W</b>e know the difference between what we have the right to do and what the right thing to do is.</p>
      </div>
    </article>

    <article class="value" style="top:542px">
      <div class="value-badge badge-relentless" role="img" aria-label="Icon of a hand snapping fingers"></div>
      <div class="value-text">
        <h2 class="value-name">Relentless</h2>
        <p class="value-desc"><b>W</b>e believe that the longer we try to do our best, the better we become.</p>
      </div>
    </article>
  </section>

  <h2 class="promise">BRAND PROMISE – TRUST, TRANSPARENCY AND DEPENDABILITY</h2>

  <section class="service service-tax">
    <div class="service-art art-tax" role="img" aria-label="Illustration of a person holding up a tax sign"></div>
    <p class="service-desc"><b>Tax</b> - Maple Finch provides all clients with a trusted tax advisor who provides accuracy in all filings and ensures your compliance with all government agencies.</p>
  </section>

  <div class="divider"></div>

  <section class="service service-accounting">
    <div class="service-art art-accounting" role="img" aria-label="Illustration of a calculator, clipboard with charts and a pen"></div>
    <p class="service-desc"><b>Accounting -</b> Maple Finch provides all business owners with the financial visibility needed to foster growth and facilitate goals.</p>
  </section>

  <div class="footer-band"></div>
</main>
</body>
</html>
```